i am a small sized carpentry business looking to generate work in decks, pergolas, small renovations including bathroom renovations or overseeing new homes being built.

Industry/Entity Type

Carpentry

Contact Information for Business Card

R M Carpentry
Marcus Elbridge
0417362815
Specialize in quality decks, pergolas, small renovations including bathrooms and housing project management.
FREE QUOTES

```html
<!DOCTYPE html>
<html lang="en">
<head>
<meta charset="utf-8">
<title>R M Carpentry – Business Card</title>
<link rel="stylesheet" href="https://fonts.googleapis.com/css2?family=Arimo:wght@400;700&display=swap">
<style>
  :root {
    --card-white: #ffffff;
    --ink-black: #111111;
    --timber-brown: #4b2a10;
    --page-bg: #ffffff;
  }
  html, body {
    margin: 0;
    padding: 0;
    width: 1200px;
    height: 784px;
    overflow: hidden;
    background: var(--page-bg);
  }
  .business-card {
    position: relative;
    width: 1200px;
    height: 784px;
    background: var(--card-white);
    font-family: "Arimo", Arial, sans-serif;
    color: var(--ink-black);
    box-sizing: border-box;
  }
  .company-name {
    position: absolute;
    left: 62px;
    top: 70px;
    margin: 0;
    font-size: 150px;
    font-weight: 700;
    letter-spacing: 4px;
    line-height: 1;
    white-space: nowrap;
  }
  .owner-name {
    position: absolute;
    left: 66px;
    top: 235px;
    margin: 0;
    font-size: 78px;
    font-weight: 400;
    letter-spacing: 1px;
    line-height: 1;
    white-space: nowrap;
  }
  .phone-number {
    position: absolute;
    left: 730px;
    top: 218px;
    margin: 0;
    font-size: 56px;
    font-weight: 400;
    letter-spacing: 1px;
    line-height: 1;
    color: var(--timber-brown);
  }
  .service-list {
    position: absolute;
    left: 66px;
    top: 548px;
    margin: 0;
    padding: 0;
    list-style: none;
    display: flex;
    align-items: center;
    font-size: 23px;
    white-space: nowrap;
  }
  .service-list li + li::before {
    content: "";
    display: inline-block;
    width: 4px;
    height: 30px;
    background: var(--ink-black);
    margin: 0 14px;
    vertical-align: -6px;
  }
  .free-quotes {
    position: absolute;
    right: 58px;
    top: 590px;
    margin: 0;
    font-size: 84px;
    font-weight: 400;
    letter-spacing: 2px;
    line-height: 1;
    color: var(--timber-brown);
  }
</style>
</head>
<body>
  <main class="business-card">
    <h1 class="company-name">R M Carpentry</h1>
    <p class="owner-name">Marcus Elbridge</p>
    <p class="phone-number">0417362815</p>
    <ul class="service-list">
      <li>Quality Decks</li>
      <li>Pergolas</li>
      <li>Small Renovations</li>
      <li>Bathrooms</li>
      <li>Housing Project Management</li>
    </ul>
    <p class="free-quotes">FREE QUOTES</p>
  </main>
</body>
</html>
```